Steel Company / Iron Railing Business Card Template

We are a custom steel fabrication company located in Trainer, PA. In business since 1979, we recently developed a new logo, and we're looking for a business card design to help display the new logo and our business. The name of the company is Kelbrook Forge Co.. The Office Phone number is (610) 555-0143. We fabricate and install custom "wrought iron" railings on our residential side, we also fabricate and erect structural steel (think cranes and steel beams in buildings) on our commercial side. Looking to get a business card template designed. Something modern, but professional. Clear and easy to read. Front should have all business and employee information including phone number(s), email address, business information, etc. back should spotlight logo.

Industry/Entity Type

Construction / Home Improvement

Contact Information for Business Card

Business information is Kelbrook Forge Co., 48 Dunmore Ave Suite 3305, Trainer, PA 19074. Phone number is (610) 555-0143. Website is www.kelbrookforge.example Business card should be for "Tom Pelling" with the job title "Sales & Estimating" but be editable for other employees. Tom's phone number is (610) 555-0178

Colors

Designer to choose colors to be used in the design.

Requirements
Must have
• Modern Feel, Design should be sized for standard business card sizing 3.5" x 2" (88.9mm x 50.8mm)

```html
<!DOCTYPE html>
<html lang="en">
<head>
<meta charset="utf-8">
<title>Kelbrook Forge Co. — Business Card</title>
<link href="https://fonts.googleapis.com/css2?family=Figtree:wght@400;700&display=swap" rel="stylesheet">
<style>
  :root {
    --page-bg: #e4e6e4;
    --card-light: #f2f2f2;
    --card-dark: #050608;
    --ink: #111111;
    --ink-reverse: #e6e6e6;
    --rule-reverse: #d8d8d8;
  }
  * { margin: 0; padding: 0; box-sizing: border-box; }
  html, body {
    width: 1200px; height: 1200px; overflow: hidden;
    background: var(--page-bg);
    font-family: "Figtree", sans-serif;
  }
  .sheet {
    position: relative; width: 1200px; height: 1200px;
  }
  .card {
    position: absolute; left: 150px; width: 900px; height: 514px;
    border-radius: 6px;
  }
  .card-front { top: 66px; background: var(--card-light); color: var(--ink); }
  .card-back { top: 620px; background: var(--card-dark); color: var(--ink-reverse); }

  .holder { position: absolute; left: 64px; top: 54px; }
  .holder-name { font-weight: 700; font-size: 33px; line-height: 1.1; }
  .holder-title { font-weight: 400; font-size: 23px; margin-top: 6px; }

  .brand-mark {
    position: absolute; display: flex; align-items: center; justify-content: center;
    gap: 14px; text-align: left;
  }
  .brand-mark .dot {
    flex: none; border-radius: 50%; border: 3px solid currentColor;
  }
  .brand-name { font-weight: 700; line-height: 1.05; }
  .card-front .brand-mark { right: 60px; top: 90px; width: 260px; }
  .card-front .brand-mark .dot { width: 42px; height: 42px; }
  .card-front .brand-name { font-size: 32px; }
  .card-back .brand-mark { left: 0; right: 0; top: 120px; }
  .card-back .brand-mark .dot { width: 60px; height: 60px; }
  .card-back .brand-name { font-size: 50px; }

  .contact-list {
    position: absolute; left: 64px; top: 330px; list-style: none;
    font-size: 23px;
  }
  .contact-list li { display: flex; align-items: center; gap: 11px; height: 32px; }
  .contact-list svg { width: 20px; height: 20px; flex: none; }

  .address {
    position: absolute; left: 569px; top: 396px;
    font-size: 23px; line-height: 32px;
  }

  .services { position: absolute; left: 0; right: 0; top: 316px; text-align: center; }
  .services-heading {
    display: inline-block; font-weight: 700; font-size: 23px;
    padding-bottom: 8px; border-bottom: 3px solid var(--rule-reverse);
  }
  .services-list {
    margin: 22px auto 0; width: 820px; font-size: 21px; line-height: 29px;
  }
</style>
</head>
<body>
<main class="sheet">

  <section class="card card-front" aria-label="Business card front">
    <div class="holder">
      <h1 class="holder-name">Tom Pelling</h1>
      <p class="holder-title">Sales &amp; Estimating</p>
    </div>

    <div class="brand-mark">
      <span class="dot"></span>
      <span class="brand-name">Kelbrook Forge Co.</span>
    </div>

    <ul class="contact-list">
      <li>
        <svg viewBox="0 0 24 24" aria-hidden="true"><path fill="currentColor" d="M6.6 10.8a15.1 15.1 0 0 0 6.6 6.6l2.2-2.2c.3-.3.7-.4 1-.2 1.1.4 2.3.6 3.6.6.6 0 1 .4 1 1V20c0 .6-.4 1-1 1A17 17 0 0 1 3 4c0-.6.4-1 1-1h3.5c.6 0 1 .4 1 1 0 1.3.2 2.5.6 3.6.1.3 0 .7-.2 1z"/></svg>
        <span>(610) 555-0143</span>
      </li>
      <li>
        <svg viewBox="0 0 24 24" aria-hidden="true"><rect x="6" y="1.5" width="12" height="21" rx="2" fill="none" stroke="currentColor" stroke-width="2"/><circle cx="12" cy="19" r="1.2" fill="currentColor"/></svg>
        <span>(610) 555-0178</span>
      </li>
      <li>
        <svg viewBox="0 0 24 24" aria-hidden="true"><path fill="currentColor" d="M2 5h20v14H2z"/><path d="M2.5 5.5 12 13l9.5-7.5" fill="none" stroke="#f2f2f2" stroke-width="2"/></svg>
        <span>info@kelbrookforge.example</span>
      </li>
      <li>
        <svg viewBox="0 0 24 24" aria-hidden="true"><g fill="none" stroke="currentColor" stroke-width="2"><circle cx="12" cy="12" r="10"/><ellipse cx="12" cy="12" rx="4" ry="10"/><path d="M2 12h20"/></g></svg>
        <span>www.kelbrookforge.example</span>
      </li>
    </ul>

    <address class="address" style="font-style:normal">
      48 Dunmore Ave Suite 3305,<br>Trainer, PA 19074
    </address>
  </section>

  <section class="card card-back" aria-label="Business card back">
    <div class="brand-mark">
      <span class="dot"></span>
      <span class="brand-name">Kelbrook Forge Co.</span>
    </div>

    <div class="services">
      <h2 class="services-heading">Our Services</h2>
      <p class="services-list">
        • wrought iron railings • structural steel • steel stairs &amp; decks • iron &amp; steel gates
        • steel fire escapes &amp; balconies • plasma cutting • window guards • steel stairs
        • balcony rails
      </p>
    </div>
  </section>

</main>
</body>
</html>
```